Searching for a captivating trade show banner design that captures the audience's attention.

I am looking to have someone design pop up trade show banner to go with my business card and flyer. Must be high resolution to print larger. See attached pics

I extended the timelines on this project.

Target Market(s)

Any commercial facility that would have fitness equipment. Park and Recreation, Fitness Centers, Multi-family, schools

Industry/Entity Type

Fitness space design and planning. fitness equipment sales. High end clients

Colors
0054AA
0677BA
7BADD7
CADEEF
E8F1F8

Requirements
Must have
• Similar look to attached business card and flyer. I would like to try and get custom look to brand. Unique cool design. I do high end facility so some type of architecture elements and or look.
Nice to have
• the smaller logo like the back of my business card somewhere on the banner design
Should not have
• clutter, dark and hard to read

```html
<!DOCTYPE html>
<html lang="en">
<head>
<meta charset="utf-8">
<title>Apex Form Studio – Trade Show Banner</title>
<link href="https://fonts.googleapis.com/css2?family=Audiowide&family=Exo+2:ital,wght@1,800;1,900&family=Poppins:wght@400;500;600&display=swap" rel="stylesheet">
<style>
  :root {
    --brand-blue: #0054aa;
    --brand-blue-mid: #2a63b8;
    --brand-blue-light: #7badd7;
    --brand-blue-pale: #cadeef;
    --ink: #1f1f22;
    --black: #050506;
    --white: #ffffff;
    --stage: #e4e5e7;
  }
  * { margin: 0; padding: 0; box-sizing: border-box; }
  html, body { width: 1200px; height: 3094px; overflow: hidden; background: var(--stage); }
  .banner {
    position: absolute; left: 20px; top: 99px;
    width: 1160px; height: 2896px;
    background: var(--white);
    box-shadow: 0 10px 40px rgba(0,0,0,.25);
    overflow: hidden;
    font-family: "Poppins", sans-serif;
  }
  .brand {
    position: absolute; left: 0; right: 0; top: 130px;
    display: flex; justify-content: center; align-items: center; gap: 22px;
  }
  .brand-mark { width: 46px; height: 46px; background: var(--brand-blue); }
  .brand-name {
    font-family: "Poppins", sans-serif; font-weight: 600;
    font-size: 50px; color: var(--ink); letter-spacing: 1px;
  }
  .consultant-name {
    position: absolute; left: 0; right: 0; top: 346px;
    text-align: center; font-family: "Audiowide", sans-serif;
    font-size: 76px; color: var(--ink); letter-spacing: 4px; word-spacing: 18px;
    font-style: italic;
  }
  .tagline-band {
    position: absolute; left: 78px; width: 1004px; top: 438px; height: 64px;
    background: linear-gradient(90deg, var(--brand-blue), var(--brand-blue-mid), var(--brand-blue));
    color: var(--white); font-size: 42px; letter-spacing: 6px;
    display: flex; align-items: center; justify-content: center;
    box-shadow: 0 4px 8px rgba(0,0,0,.25);
  }
  .headline-top {
    position: absolute; left: 0; right: 0; top: 510px;
    text-align: center; font-family: "Exo 2", sans-serif; font-style: italic; font-weight: 900;
    font-size: 178px; line-height: 1; color: var(--ink); letter-spacing: 2px;
  }
  .headline-bottom {
    position: absolute; left: 0; right: 0; top: 690px;
    text-align: center; font-family: "Audiowide", sans-serif; font-style: italic;
    font-size: 150px; line-height: 1; color: var(--brand-blue); letter-spacing: 4px;
  }
  .venue-photo {
    position: absolute; left: 91px; top: 884px; width: 982px; height: 756px;
    background: linear-gradient(180deg, #eef1f4 0%, #d8dde2 45%, #9a8a7a 75%, #8a6a50 100%);
    border: 4px solid var(--white);
    box-shadow: 0 6px 14px rgba(0,0,0,.3);
    z-index: 2;
  }
  .offerings-panel {
    position: absolute; left: 0; right: 0; top: 1601px; height: 1068px;
    background: var(--black);
  }
  .offerings-title {
    position: absolute; left: 84px; width: 999px; top: 1676px; height: 100px;
    background: linear-gradient(90deg, var(--brand-blue), var(--brand-blue-mid), var(--brand-blue));
    color: var(--white); font-family: "Audiowide", sans-serif; font-style: italic;
    font-size: 66px; letter-spacing: 6px;
    display: flex; align-items: center; justify-content: center;
  }
  .grid-line-v {
    position: absolute; left: 551px; top: 1832px; height: 703px;
    border-left: 3px dashed #9a9a9a;
  }
  .grid-line-h {
    position: absolute; left: 149px; width: 808px; top: 2165px;
    border-top: 3px dashed #9a9a9a;
  }
  .offering { position: absolute; width: 460px; text-align: center; color: var(--white); }
  .offering-icon {
    width: 168px; height: 168px; margin: 0 auto;
    border-radius: 50%; border: 6px solid var(--white);
    background: var(--brand-blue-mid);
    display: flex; align-items: center; justify-content: center;
  }
  .offering-icon svg { width: 96px; height: 96px; }
  .offering-label { margin-top: 20px; font-size: 40px; line-height: 46px; font-weight: 500; }
  .offering.col-left { left: 88px; }
  .offering.col-right { left: 588px; }
  .offering.row-top { top: 1832px; }
  .offering.row-bottom { top: 2216px; }
  .phone-band {
    position: absolute; left: 78px; width: 1004px; top: 2606px; height: 116px;
    background: linear-gradient(90deg, var(--brand-blue), var(--brand-blue-mid), var(--brand-blue));
    display: flex; align-items: center; justify-content: center; gap: 28px;
    color: var(--white); font-family: "Audiowide", sans-serif;
    font-size: 82px; letter-spacing: 4px; word-spacing: 20px;
    box-shadow: 0 4px 10px rgba(0,0,0,.35);
  }
  .phone-band svg { width: 70px; height: 70px; }
  .web-address {
    position: absolute; left: 0; right: 0; top: 2782px;
    text-align: center; font-size: 64px; letter-spacing: 10px; color: var(--ink);
  }
  .web-address strong { color: var(--brand-blue); font-weight: 600; }
</style>
</head>
<body>
<main class="banner">
  <div class="brand">
    <span class="brand-mark"></span>
    <span class="brand-name">APEX FORM STUDIO</span>
  </div>

  <h1 class="consultant-name">DANA WHITLOW</h1>
  <div class="tagline-band">FITNESS CONSULTANT EXPERT FOR</div>
  <div class="headline-top">FITNESS</div>
  <div class="headline-bottom">SPACES</div>

  <div class="venue-photo" role="img" aria-label="Bright commercial gym interior with weight racks, benches and tall windows"></div>

  <section class="offerings-panel"></section>
  <h2 class="offerings-title">OUR OFFERINGS</h2>
  <div class="grid-line-v"></div>
  <div class="grid-line-h"></div>

  <div class="offering col-left row-top">
    <div class="offering-icon">
      <svg viewBox="0 0 48 48" fill="none" stroke="#fff" stroke-width="3" stroke-linecap="round">
        <path d="M17 28a10 10 0 1 1 14 0c-2 2-3 3-3 6h-8c0-3-1-4-3-6z"/>
        <path d="M20 38h8M21 42h6"/>
        <path d="M24 4v3M8 14l3 2M40 14l-3 2"/>
      </svg>
    </div>
    <p class="offering-label">Conceptual<br>Planning</p>
  </div>

  <div class="offering col-right row-top">
    <div class="offering-icon">
      <svg viewBox="0 0 48 48" fill="none" stroke="#fff" stroke-width="3" stroke-linecap="round" stroke-linejoin="round">
        <path d="M4 20l8-8 8 4 6-4 6 2 12 10"/>
        <path d="M12 12l-4 14 10 10 4-2 4 2 12-12"/>
        <path d="M20 28l6 6M24 24l6 6"/>
      </svg>
    </div>
    <p class="offering-label">3rd Party<br>Collaboration</p>
  </div>

  <div class="offering col-left row-bottom">
    <div class="offering-icon">
      <svg viewBox="0 0 48 48" fill="none" stroke="#fff" stroke-width="3" stroke-linejoin="round">
        <path d="M21 4h6l1 5 4 2 4-3 4 4-3 4 2 4 5 1v6l-5 1-2 4 3 4-4 4-4-3-4 2-1 5h-6l-1-5-4-2-4 3-4-4 3-4-2-4-5-1v-6l5-1 2-4-3-4 4-4 4 3 4-2z"/>
        <circle cx="24" cy="24" r="6"/>
      </svg>
    </div>
    <p class="offering-label">Equipment<br>Specifications<br>and Procurement</p>
  </div>

  <div class="offering col-right row-bottom">
    <div class="offering-icon">
      <svg viewBox="0 0 48 48" fill="none" stroke="#fff" stroke-width="3" stroke-linecap="round" stroke-linejoin="round">
        <circle cx="24" cy="24" r="18" stroke-dasharray="6 4"/>
        <path d="M30 12a7 7 0 0 0-8 9L13 30a3 3 0 0 0 5 5l9-9a7 7 0 0 0 9-8l-4 4-4-1-1-4z"/>
      </svg>
    </div>
    <p class="offering-label">Preventative<br>Maintenance Service</p>
  </div>

  <div class="phone-band">
    <svg viewBox="0 0 48 48">
      <circle cx="24" cy="24" r="22" fill="#fff"/>
      <path d="M16 12l5 0 2 7-3 3c2 4 5 7 9 9l3-3 7 2v5c0 2-2 3-4 3-12-1-21-10-22-22 0-2 1-4 3-4z" fill="#0054aa"/>
    </svg>
    <span>555 014 2386</span>
  </div>

  <p class="web-address">www.<strong>apexformstudio</strong>.co</p>
</main>
</body>
</html>
```